Brisbane IT support business needs our first website

Hi All,

We are after a new website design for our IT solutions and support business.The business name is Harlow Digital Systems Group, or HDSG for short. We provide a range of solutions and services within the IT space.

I would like to utilize the two colours in our business logo I have uploaded.

I understand this is initially for the design only aspect of the site, but I would like to engage the winner to finish coding the website and finalize after also.

Target Market(s)

Other businesses owners and home users.

Industry/Entity Type

Business

Requirements
Must have
• Nice clean and functional design utilizing our business colours from the logo.

```html
<!DOCTYPE html>
<html lang="en">
<head>
<meta charset="utf-8">
<title>Harlow Digital Systems Group</title>
<link href="https://fonts.googleapis.com/css2?family=Lato:wght@300;400;700&display=swap" rel="stylesheet">
<style>
  :root {
    --orange: #f07f1e;
    --orange-dark: #d96a0c;
    --navy: #0f4a6b;
    --ink: #3b3b3b;
    --muted: #8a8a8a;
    --paper: #ffffff;
    --mist: #f1f1f1;
    --line: #e0e0e0;
  }
  * { box-sizing: border-box; margin: 0; padding: 0; }
  html, body { width: 1200px; height: 2720px; overflow: hidden; }
  body { font-family: "Lato", sans-serif; color: var(--ink); background: var(--paper); position: relative; }
  section, header, footer { position: absolute; left: 0; width: 1200px; }

  /* Hero */
  .hero { top: 0; height: 600px; overflow: hidden; }
  .hero-photo { position: absolute; inset: 0; background: radial-gradient(ellipse at 70% 55%, #f9a34d 0%, #ef7f1f 45%, #c85f0a 100%); }
  .brand { position: absolute; left: 128px; top: 0; width: 290px; height: 136px; background: var(--paper); display: flex; align-items: center; justify-content: center; }
  .brand-name { font-size: 38px; font-weight: 400; color: var(--navy); letter-spacing: 3px; }
  .nav { position: absolute; left: 420px; top: 28px; display: flex; }
  .nav a { color: var(--paper); text-decoration: none; font-size: 17px; padding: 14px 20px; }
  .nav a.active { background: var(--orange-dark); }
  .hero-caption { position: absolute; left: 280px; top: 262px; width: 640px; height: 172px; border: 3px solid rgba(255,255,255,.85); background: rgba(255,255,255,.08); text-align: center; color: var(--paper); font-weight: 300; font-size: 44px; line-height: 64px; padding-top: 20px; }
  .hero-btn { position: absolute; left: 532px; top: 452px; width: 136px; height: 40px; background: var(--navy); color: var(--paper); font-size: 15px; display: flex; align-items: center; justify-content: center; }
  .hero-arrow { position: absolute; top: 332px; width: 44px; height: 44px; background: rgba(0,0,0,.25); }
  .hero-arrow.left { left: 128px; } .hero-arrow.right { right: 128px; }
  .dots { position: absolute; top: 562px; left: 0; width: 100%; display: flex; justify-content: center; gap: 10px; }
  .dots span { width: 16px; height: 16px; border-radius: 50%; border: 2px solid var(--paper); }
  .dots span.on { background: var(--paper); }

  .section-title { text-align: center; font-size: 40px; font-weight: 400; letter-spacing: 1px; }
  .section-sub { text-align: center; font-size: 15px; letter-spacing: 5px; margin-top: 14px; }

  /* Services */
  .services { top: 600px; height: 560px; padding-top: 72px; }
  .services .section-title { color: var(--navy); }
  .services .section-sub { color: var(--muted); }
  .service-list { display: flex; justify-content: center; gap: 40px; margin-top: 54px; }
  .service { width: 190px; text-align: center; }
  .service-icon { width: 116px; height: 116px; border-radius: 50%; background: var(--orange); margin: 0 auto; display: flex; align-items: center; justify-content: center; }
  .service h3 { font-size: 17px; font-weight: 400; color: var(--ink); margin-top: 18px; line-height: 22px; text-transform: uppercase; }
  .service p { font-size: 12px; color: var(--muted); line-height: 17px; margin-top: 12px; }

  /* Solutions */
  .solutions { top: 1160px; height: 540px; background: var(--navy); color: var(--paper); padding-top: 48px; }
  .solutions .section-sub { color: #c7d6e0; }
  .solution-list { display: flex; justify-content: center; gap: 66px; margin-top: 46px; }
  .solution { width: 262px; }
  .solution-photo { height: 168px; background: linear-gradient(135deg, #dfe6ea, #9fb2be); }
  .solution h3 { font-size: 19px; font-weight: 400; margin-top: 26px; }
  .solution p { font-size: 13px; color: #c7d6e0; margin-top: 8px; }
  .solutions .btn { position: absolute; left: 536px; top: 456px; }
  .btn { width: 128px; height: 40px; background: var(--orange); color: var(--paper); font-size: 15px; display: flex; align-items: center; justify-content: center; gap: 8px; }

  /* Clients */
  .clients { top: 1700px; height: 520px; background: var(--mist); padding-top: 40px; }
  .clients .section-title { color: var(--navy); }
  .clients .section-sub { color: var(--muted); }
  .quote-list { display: flex; justify-content: center; gap: 40px; margin-top: 46px; }
  .quote { position: relative; width: 450px; height: 280px; background: var(--paper); text-align: center; padding-top: 20px; }
  .quote-mark { position: absolute; top: 18px; font-size: 60px; color: var(--line); font-family: Georgia, serif; line-height: 1; }
  .quote-mark.open { left: 26px; } .quote-mark.close { right: 26px; top: 200px; }
  .avatar { width: 68px; height: 68px; border-radius: 50%; background: linear-gradient(#c9ced3, #9aa3ab); margin: 0 auto; border: 3px solid var(--line); }
  .quote h4 { font-size: 17px; font-weight: 400; margin-top: 16px; }
  .quote .role { font-size: 13px; color: var(--muted); margin-top: 4px; }
  .quote p { font-size: 12px; color: var(--muted); line-height: 17px; padding: 0 56px; margin-top: 18px; }

  /* CTA */
  .cta { top: 2220px; height: 260px; background: var(--orange); color: var(--paper); padding-top: 70px; }
  .cta .section-title { font-size: 36px; font-weight: 300; }
  .cta .section-sub { letter-spacing: 5px; margin-top: 16px; }
  .cta .btn { position: absolute; left: 532px; top: 168px; background: var(--paper); color: var(--orange); width: 136px; }

  /* Footer */
  .site-footer { top: 2480px; height: 180px; background: var(--mist); }
  .footer-col { position: absolute; top: 40px; }
  .footer-col h5 { font-size: 13px; font-weight: 700; letter-spacing: 1px; color: var(--ink); padding-bottom: 8px; position: relative; }
  .footer-col h5::after { content: ""; position: absolute; left: 0; bottom: 0; width: 28px; height: 2px; background: var(--orange); }
  .footer-col p { font-size: 13px; color: var(--muted); line-height: 20px; margin-top: 10px; }
  .social { display: flex; gap: 8px; margin-top: 14px; }
  .social span { width: 28px; height: 28px; border-radius: 50%; background: var(--navy); }
  .social span:nth-child(2) { background: #2a8fbd; }
  .social span:nth-child(3) { background: #3e9fd0; }
  .social span:nth-child(4) { background: var(--orange); }
  .legal { position: absolute; left: 0; width: 1200px; top: 2660px; height: 60px; background: #e6e6e6; text-align: center; padding-top: 12px; }
  .legal strong { display: block; font-size: 14px; font-weight: 400; color: var(--ink); }
  .legal small { font-size: 11px; color: var(--muted); }
</style>
</head>
<body>

<header class="hero">
  <div class="hero-photo" role="img" aria-label="Orange-toned photo of hands using a tablet with floating app icons"></div>
  <div class="brand"><span class="brand-name">HDSG</span></div>
  <nav class="nav">
    <a class="active">Home</a><a>About us</a><a>Services</a><a>Technology</a><a>Solutions</a><a>Support</a><a>Contact</a>
  </nav>
  <div class="hero-arrow left"><svg width="44" height="44" viewBox="0 0 44 44"><path d="M26 13 L17 22 L26 31" fill="none" stroke="#fff" stroke-width="3"/></svg></div>
  <div class="hero-arrow right"><svg width="44" height="44" viewBox="0 0 44 44"><path d="M18 13 L27 22 L18 31" fill="none" stroke="#fff" stroke-width="3"/></svg></div>
  <div class="hero-caption">Generating Innovative Ideas<br>Backed by Leading Technology</div>
  <div class="hero-btn">View Portfolio &nbsp;→</div>
  <div class="dots"><span class="on"></span><span></span><span></span></div>
</header>

<section class="services">
  <h2 class="section-title">OUR SERVICES</h2>
  <p class="section-sub">TRUSTED IT SOLUTIONS</p>
  <div class="service-list">
    <div class="service">
      <div class="service-icon"><svg width="52" height="52" viewBox="0 0 52 52" fill="none" stroke="#fff" stroke-width="3"><path d="M6 26 L16 18 L26 24 L36 18 L46 26 L34 36 L26 30 L18 36 Z"/></svg></div>
      <h3>Premium<br>IT Solutions</h3>
      <p>Lorem ipsum dolor sit amet, consectetur adipiscing elit, sed diam nonummy nibh euismod tincidunt ut laoreet dolore magna aliquam erat.</p>
    </div>
    <div class="service">
      <div class="service-icon"><svg width="52" height="52" viewBox="0 0 52 52" fill="none" stroke="#fff" stroke-width="3"><rect x="8" y="10" width="36" height="24" rx="2"/><path d="M20 42 H32 M26 34 V42"/></svg></div>
      <h3>Web<br>Development</h3>
      <p>Lorem ipsum dolor sit amet, consectetur adipiscing elit, sed diam nonummy nibh euismod tincidunt ut laoreet dolore magna aliquam erat.</p>
    </div>
    <div class="service">
      <div class="service-icon"><svg width="52" height="52" viewBox="0 0 52 52" fill="none" stroke="#fff" stroke-width="3"><ellipse cx="26" cy="12" rx="14" ry="5"/><path d="M12 12 V40 C12 46 40 46 40 40 V12 M12 26 C12 32 40 32 40 26"/></svg></div>
      <h3>Database<br>Management</h3>
      <p>Lorem ipsum dolor sit amet, consectetur adipiscing elit, sed diam nonummy nibh euismod tincidunt ut laoreet dolore magna aliquam erat.</p>
    </div>
    <div class="service">
      <div class="service-icon"><svg width="52" height="52" viewBox="0 0 52 52" fill="none" stroke="#fff" stroke-width="3"><path d="M12 40 L30 22 M36 10 A8 8 0 1 0 42 16 M14 12 L40 38"/></svg></div>
      <h3>Technical<br>Support</h3>
      <p>Lorem ipsum dolor sit amet, consectetur adipiscing elit, sed diam nonummy nibh euismod tincidunt ut laoreet dolore magna aliquam erat.</p>
    </div>
  </div>
</section>

<section class="solutions">
  <h2 class="section-title">SOLUTIONS</h2>
  <p class="section-sub">WE TAKE PRIDE IN OUR WORK</p>
  <div class="solution-list">
    <div class="solution">
      <div class="solution-photo" role="img" aria-label="Photo of a team meeting around an office table"></div>
      <h3>Job Management</h3>
      <p>Lorem ipsum dolor sit amet conse.</p>
    </div>
    <div class="solution">
      <div class="solution-photo" role="img" aria-label="Photo of a business handshake"></div>
      <h3>Business Management</h3>
      <p>Lorem ipsum dolor sit amet conse.</p>
    </div>
    <div class="solution">
      <div class="solution-photo" role="img" aria-label="Photo of a customer relationship meeting"></div>
      <h3>Customer Relationship</h3>
      <p>Lorem ipsum dolor sit amet conse.</p>
    </div>
  </div>
  <div class="btn">View More <svg width="14" height="12" viewBox="0 0 14 12"><path d="M1 6 H12 M8 2 L12 6 L8 10" fill="none" stroke="#fff" stroke-width="2"/></svg></div>
</section>

<section class="clients">
  <h2 class="section-title">WHAT OUR CLIENTS ARE SAYING</h2>
  <p class="section-sub">DON'T JUST TAKE OUR WORDS</p>
  <div class="quote-list">
    <div class="quote">
      <span class="quote-mark open">&ldquo;</span>
      <div class="avatar" role="img" aria-label="Client portrait"></div>
      <h4>Mr Lorem Ipsum</h4>
      <div class="role">Art officer</div>
      <p>Lorem ipsum dolor sit amet, consectetur adipiscing elit, sed diam nonummy nibh euismod tincidunt ut laoreet dolore magna aliquam erat volutpat ut wisi enim ad minim veniam.</p>
      <span class="quote-mark close">&rdquo;</span>
    </div>
    <div class="quote">
      <span class="quote-mark open">&ldquo;</span>
      <div class="avatar" role="img" aria-label="Client portrait"></div>
      <h4>Miss Lorem Ipsum</h4>
      <div class="role">Marketing Manager</div>
      <p>Lorem ipsum dolor sit amet, consectetur adipiscing elit, sed diam nonummy nibh euismod tincidunt ut laoreet dolore magna aliquam erat volutpat ut wisi enim ad minim veniam.</p>
      <span class="quote-mark close">&rdquo;</span>
    </div>
  </div>
</section>

<section class="cta">
  <h2 class="section-title">WE CAN HELP BUILD YOUR PROJECT</h2>
  <p class="section-sub">TELL US ABOUT YOUR PROJECT</p>
  <div class="btn">Contact us <svg width="14" height="12" viewBox="0 0 14 12"><path d="M1 6 H12 M8 2 L12 6 L8 10" fill="none" stroke="#f07f1e" stroke-width="2"/></svg></div>
</section>

<footer class="site-footer">
  <div class="footer-col" style="left:132px"><h5>ADDRESS</h5><p>212 Corran Avenue, Riverbend,<br>AU 5120</p></div>
  <div class="footer-col" style="left:420px"><h5>PHONE</h5><p>07 5550 1284</p></div>
  <div class="footer-col" style="left:620px"><h5>EMAIL</h5><p>contact@hdsg-systems.com</p></div>
  <div class="footer-col" style="left:904px"><h5>FOLLOW US</h5><div class="social"><span></span><span></span><span></span><span></span></div></div>
</footer>
<div class="legal">
  <strong>Harlow Digital Systems Group</strong>
  <small>© 2014 · All Rights Reserved.</small>
</div>

</body>
</html>
```